Need a business card design for a residential architect.

You can get a sense of his work at www.tbrelloway.com

Would like a consistent look and feel between business card and website
.

Target Market(s)

Residential homeowners builders

Industry/Entity Type

Residential

Contact Information for Business Card

Dale Brelloway
Principle
Brelloway Architecture
418 Quillfern Lane
Menlo Park, CA 94025

dale@tbrelloway.com

tbrelloway.com
phone: 650-555-0172
Fax: 650-555-0194

Font styles to use
Sans Serif

Requirements
Must have
• Details above
Nice to have
• Would like a consistent look and feel between business card and website
Should not have
• None

```html
<!DOCTYPE html>
<html lang="en">
<head>
<meta charset="utf-8">
<title>Brelloway Architecture – Business Card</title>
<link href="https://fonts.googleapis.com/css2?family=Open+Sans:wght@400;600&display=swap" rel="stylesheet">
<style>
  :root {
    --page-bg: #e9e9e9;
    --card-top: #ffffff;
    --card-bottom: #ececec;
    --band-gray: #a9a9a9;
    --swoosh-dark: #4a4a4a;
    --ink: #3a3a3a;
    --ink-soft: #5c5c5c;
    --brand-gray: #5a5a5a;
    --icon-bg: #3d3d3d;
    --icon-fg: #ffffff;
    --divider: #8a8a8a;
  }
  html, body {
    margin: 0;
    width: 1200px;
    height: 899px;
    overflow: hidden;
    background: var(--page-bg);
    font-family: "Open Sans", Arial, sans-serif;
  }
  .business-card {
    position: absolute;
    left: 150px;
    top: 192px;
    width: 900px;
    height: 514px;
    border-radius: 46px;
    overflow: hidden;
    background: linear-gradient(180deg, var(--card-top) 0%, var(--card-bottom) 100%);
    box-shadow: 0 6px 22px rgba(0,0,0,0.12);
  }
  .card-bands {
    position: absolute;
    left: 0; top: 0;
    width: 900px; height: 514px;
  }
  .brand-name {
    position: absolute;
    top: 88px;
    left: 0;
    width: 100%;
    text-align: center;
    padding-left: 60px;
    box-sizing: border-box;
    font-size: 44px;
    font-weight: 400;
    letter-spacing: 5px;
    text-transform: uppercase;
    color: var(--brand-gray);
  }
  .person {
    position: absolute;
    right: 492px;
    top: 196px;
    text-align: right;
    color: var(--ink);
  }
  .person-name {
    font-size: 22px;
    font-weight: 600;
    line-height: 30px;
    margin: 0;
  }
  .person-title {
    font-size: 17px;
    line-height: 24px;
    color: var(--ink-soft);
    margin: 0;
  }
  .person-address {
    font-size: 17px;
    line-height: 30px;
    color: var(--ink-soft);
    margin: 22px 0 0;
  }
  .divider {
    position: absolute;
    left: 425px;
    top: 196px;
    width: 1.5px;
    height: 160px;
    background: var(--divider);
  }
  .contact-list {
    position: absolute;
    left: 444px;
    top: 196px;
    margin: 0;
    padding: 0;
    list-style: none;
    font-size: 17px;
    color: var(--ink);
  }
  .contact-list li {
    display: flex;
    align-items: center;
    height: 30px;
  }
  .contact-icon {
    width: 20px;
    height: 20px;
    margin-right: 10px;
    flex: none;
  }
</style>
</head>
<body>
  <div class="business-card">
    <svg class="card-bands" viewBox="0 0 900 514" aria-hidden="true">
      <path d="M0 414 Q 420 392 900 482 L900 514 L0 514 Z" fill="var(--band-gray)"/>
      <path d="M0 388 Q 430 362 900 470 Q 430 378 0 400 Z" fill="var(--swoosh-dark)"/>
    </svg>

    <div class="brand-name">Brelloway Architecture</div>

    <div class="person">
      <p class="person-name">Dale Brelloway</p>
      <p class="person-title">Principle</p>
      <p class="person-address">418 Quillfern Lane<br>Menlo Park, CA 94025</p>
    </div>

    <div class="divider"></div>

    <ul class="contact-list">
      <li>
        <svg class="contact-icon" viewBox="0 0 20 20"><circle cx="10" cy="10" r="10" fill="var(--icon-bg)"/><path d="M6.5 5.5 L8.5 5.2 L9.4 7.6 L8.2 8.6 Q9.2 10.9 11.4 11.8 L12.4 10.6 L14.8 11.5 L14.5 13.5 Q9 14 6.5 5.5 Z" fill="var(--icon-fg)"/></svg>
        650-555-0172
      </li>
      <li>
        <svg class="contact-icon" viewBox="0 0 20 20"><circle cx="10" cy="10" r="10" fill="var(--icon-bg)"/><rect x="5" y="8" width="10" height="6" fill="var(--icon-fg)"/><rect x="7" y="5" width="6" height="3" fill="var(--icon-fg)"/><rect x="7" y="12" width="6" height="3" fill="var(--icon-bg)"/></svg>
        650-555-0194
      </li>
      <li>
        <svg class="contact-icon" viewBox="0 0 20 20"><circle cx="10" cy="10" r="10" fill="var(--icon-bg)"/><rect x="7" y="4.5" width="6" height="11" rx="1.2" fill="var(--icon-fg)"/><rect x="8" y="6" width="4" height="7" fill="var(--icon-bg)"/></svg>
        650-555-0138
      </li>
      <li>
        <svg class="contact-icon" viewBox="0 0 20 20"><circle cx="10" cy="10" r="10" fill="var(--icon-bg)"/><rect x="5" y="6.5" width="10" height="7" fill="var(--icon-fg)"/><path d="M5 6.5 L10 10.5 L15 6.5" fill="none" stroke="var(--icon-bg)" stroke-width="1"/></svg>
        dale@tbrelloway.com
      </li>
      <li>
        <svg class="contact-icon" viewBox="0 0 20 20"><circle cx="10" cy="10" r="10" fill="var(--icon-bg)"/><circle cx="10" cy="10" r="5.5" fill="none" stroke="var(--icon-fg)" stroke-width="1.2"/><ellipse cx="10" cy="10" rx="2.4" ry="5.5" fill="none" stroke="var(--icon-fg)" stroke-width="1"/><line x1="4.5" y1="10" x2="15.5" y2="10" stroke="var(--icon-fg)" stroke-width="1"/></svg>
        www.tbrelloway.com
      </li>
    </ul>
  </div>
</body>
</html>
```